Custom Framing Shop Tallpine Framing Studio

I want an eye catching graphic that will be used a s business sign on a busy road. The sign MUST communicate the type of business it is clearly to vehicles traveling at 40 mph. This is a custom picture framing business and the sign will be hanging and be approximately 32" X 48". The business name is Tallpine Framing Studio; Custom framing: by appointment and should include a whole or partial image of a picture frame as a visual que. I've included inspiration idea's, color pallets and styles that I like and a current business card for inspiration. I like the crimson font style shadowing and background colors of the attached Olans pizzeria sign. I'd prefer crimson letters. Custom Framing is the message to communicate, followed by phone number and business name. I like the idea of a shield shape with a banner since it would more eye catching, Once again the Tallpine image and name is less important than communicating what the business does. I like Crimson, grey, gold, black but am open to new ideas . I like the idea of a shield with a banner more than a rectangle, but am open to idea's

Target Market(s)

My target market is local homeowners ($700k+) who want a relationship with their framer and are willing to pay for a customized experience compared to a craft store experience. I have more female clients then men.

Industry/Entity Type

Picture Framing Art

Other font styles liked:
• Look at the attached image of a custom pizzeria sign, its kid of a custom car pinstripe font style. Script and decorative may be difficult to read while driving by but add to the elegance.

Colors

Designer to choose colors to be used in the design.

Requirements
Must have
• Clearly communicate what the business does "Custom framing" preferably with a picture frame and words
Nice to have
• incorporate a Tallpine into the graphic
Should not have
• A Tallpine image doesn't communicate what the business does to a vehicle traveling at 40 mph by the sign

```html
<!DOCTYPE html>
<html lang="en">
<head>
<meta charset="utf-8">
<title>Tallpine Framing Studio – Sign</title>
<link rel="stylesheet" href="https://fonts.googleapis.com/css2?family=Graduate&family=Orbitron:wght@800;900&family=Montserrat:wght@700&family=Roboto:wght@400&display=swap">
<style>
  :root{
    --paper:#ffffff;
    --frame-brown:#5e2f0e;
    --panel-tan:#8a6c40;
    --crimson:#5a0f12;
    --crimson-shadow:#b08a5a;
    --ink:#111111;
    --white:#ffffff;
    --dim-line:#333333;
  }
  html,body{margin:0;padding:0;overflow:hidden;background:var(--paper);}
  .canvas{width:1200px;height:1001px;display:block;}
  .dimension-line{stroke:var(--dim-line);stroke-width:2;fill:none;}
  .dimension-label{font-family:'Roboto',Arial,sans-serif;font-size:38px;fill:var(--ink);}
  .badge-outer{fill:var(--frame-brown);}
  .badge-inner{fill:var(--panel-tan);}
  .badge-name{font-family:'Graduate',serif;font-size:60px;fill:var(--crimson);}
  .shield-outer{fill:var(--frame-brown);}
  .shield-panel{fill:var(--panel-tan);}
  .headline{font-family:'Graduate',serif;font-size:104px;}
  .headline-shadow{fill:var(--crimson-shadow);}
  .headline-main{fill:var(--crimson);}
  .tagline{font-family:'Montserrat',Arial,sans-serif;font-weight:700;font-size:19px;fill:var(--ink);}
  .rule{stroke:var(--ink);stroke-width:4;}
  .phone{font-family:'Orbitron',Arial,sans-serif;font-weight:900;font-size:58px;fill:var(--ink);}
  .phone-icon{fill:none;stroke:var(--ink);stroke-width:3;}
  .banner{fill:var(--crimson);}
  .banner-text{font-family:'Orbitron',Arial,sans-serif;font-weight:800;font-size:31px;fill:var(--white);}
</style>
</head>
<body>
<svg class="canvas" viewBox="0 0 1500 1251.25" xmlns="http://www.w3.org/2000/svg">
  <!-- width dimension -->
  <g class="dimension dimension-width">
    <line class="dimension-line" x1="283" y1="213" x2="700" y2="213"/>
    <line class="dimension-line" x1="840" y1="213" x2="1258" y2="213"/>
    <line class="dimension-line" x1="283" y1="190" x2="283" y2="236"/>
    <line class="dimension-line" x1="1258" y1="190" x2="1258" y2="236"/>
    <text class="dimension-label" x="771" y="227" text-anchor="middle">48"</text>
  </g>
  <!-- height dimension -->
  <g class="dimension dimension-height">
    <line class="dimension-line" x1="180" y1="280" x2="180" y2="546"/>
    <line class="dimension-line" x1="180" y1="655" x2="180" y2="921"/>
    <line class="dimension-line" x1="157" y1="280" x2="203" y2="280"/>
    <line class="dimension-line" x1="157" y1="921" x2="203" y2="921"/>
    <text class="dimension-label" x="188" y="615" text-anchor="middle">32"</text>
  </g>

  <!-- round badge -->
  <g class="badge">
    <circle class="badge-outer" cx="777" cy="492" r="204"/>
    <circle class="badge-inner" cx="777" cy="492" r="182"/>
    <text class="badge-name" x="777" y="505" text-anchor="middle">Tallpine</text>
  </g>

  <!-- shield -->
  <g class="shield">
    <path class="shield-outer" d="M297 590 L1258 590 L1222 786 L1190 786 L1178 853 L1128 862 L1140 921 Q960 895 910 895 L777 916 L640 893 Q560 895 413 921 L425 862 L383 853 L372 786 L330 786 Z"/>
    <path class="shield-panel" d="M322 613 L1232 613 L1204 766 L1170 766 L1156 836 L1020 850 L777 870 L534 850 L400 836 L386 766 L352 766 Z"/>
  </g>

  <!-- headline -->
  <g class="headline">
    <text class="headline-shadow" x="387" y="720" textLength="795" lengthAdjust="spacingAndGlyphs">CUSTOM FRAMING</text>
    <text class="headline-main" x="382" y="715" textLength="795" lengthAdjust="spacingAndGlyphs">CUSTOM FRAMING</text>
  </g>

  <!-- tagline -->
  <g class="tagline-row">
    <line class="rule" x1="388" y1="740" x2="596" y2="740"/>
    <text class="tagline" x="612" y="747" textLength="330" lengthAdjust="spacing">BY APPOINTMENT</text>
    <line class="rule" x1="966" y1="740" x2="1172" y2="740"/>
  </g>

  <!-- phone -->
  <g class="phone-row">
    <g class="phone-icon">
      <circle cx="458" cy="781" r="14"/>
      <path d="M451 773 q-2 4 2 10 q5 7 11 7 l2 -3 l-4 -3 l-2 2 q-4 -2 -6 -6 l2 -2 l-3 -4 Z" stroke-width="2"/>
    </g>
    <text class="phone" x="487" y="800" textLength="625" lengthAdjust="spacingAndGlyphs">(555) 014-2290</text>
  </g>

  <!-- banner -->
  <g class="banner-ribbon">
    <path class="banner" d="M437 840 Q777 800 1117 840 L1108 895 Q777 855 448 895 Z"/>
    <path id="banner-curve" d="M478 868 Q777 832 1076 868" fill="none"/>
    <text class="banner-text">
      <textPath href="#banner-curve" startOffset="50%" text-anchor="middle" textLength="595" lengthAdjust="spacingAndGlyphs">TALLPINE FRAMING STUDIO</textPath>
    </text>
  </g>
</svg>
</body>
</html>
```